Designs of screens for job search mobile app

Design the following screens:

1. Login
2. Job search results in tabs
3. Job details in cards format
4. Profile
5. Settings

Logo and references are provided. The app need to be playful, easy to use, different from traditional job search app like Hirevo, Workbrix and others and targeted to Millennial users (age 18-30).

The main app reference is Pogura, in terms of the colorful and fun color and font scheme.

Target Market(s)

Millennial users (age 18-30).

Requirements
Must have
• A fun, playful feel

```html
<!DOCTYPE html>
<html lang="en">
<head>
<meta charset="utf-8">
<title>Job Details Screen</title>
<link href="https://fonts.googleapis.com/css2?family=Oswald:wght@300;400&display=swap" rel="stylesheet">
<style>
  :root {
    --page-bg: #1f93d3;
    --screen-teal: #35bdd7;
    --card-white: #ffffff;
    --peek-grey: #ececec;
    --accent-cyan: #2fb6d6;
    --text-dark: #3a3a3a;
    --text-muted: #6f6f6f;
    --brand-red: #8a1c1c;
    --skill-blue: #4a8fd8;
    --skill-pink: #ec3f9a;
    --skill-green: #3fd98a;
    --avatar-warm: #b9876a;
    --avatar-cool: #8a7f7a;
    --avatar-olive: #9a8a5e;
    --avatar-deep: #6b4a3a;
    --avatar-light: #c9b3a0;
  }
  * { box-sizing: border-box; margin: 0; padding: 0; }
  html, body {
    width: 1200px; height: 822px; overflow: hidden;
    background: var(--page-bg);
    font-family: "Oswald", "Arial Narrow", sans-serif;
    font-weight: 300;
  }
  .app-screen {
    position: absolute; left: 400px; top: 50px;
    width: 400px; height: 720px;
    background: var(--screen-teal);
    color: #fff;
    overflow: hidden;
    box-shadow: 0 20px 40px rgba(0,40,90,.35);
  }
  .status-bar {
    position: absolute; top: 6px; left: 12px; right: 12px;
    display: flex; justify-content: space-between; align-items: center;
    font-size: 11px; font-weight: 400;
  }
  .status-carrier, .status-battery { display: flex; align-items: center; gap: 4px; }
  .header {
    position: absolute; top: 28px; left: 0; right: 0; height: 40px;
    display: flex; align-items: center; justify-content: center;
  }
  .header-title { font-size: 17px; letter-spacing: .5px; }
  .header-close { position: absolute; left: 18px; top: 10px; }
  .header-exit { position: absolute; right: 18px; top: 10px; }
  .peek-card {
    position: absolute; width: 14px; background: var(--peek-grey);
    top: 170px; height: 350px;
  }
  .peek-left { left: 0; border-radius: 0 6px 6px 0; }
  .peek-right { right: 0; border-radius: 6px 0 0 6px; }
  .job-card {
    position: absolute; left: 28px; right: 28px; top: 82px; height: 478px;
    background: var(--card-white); border-radius: 8px;
    padding: 22px 22px; color: var(--text-dark);
  }
  .card-top { display: flex; justify-content: space-between; align-items: flex-start; }
  .job-title { color: var(--accent-cyan); font-size: 20px; font-weight: 300; letter-spacing: .3px; }
  .company-name {
    display: flex; align-items: center; gap: 5px;
    color: var(--brand-red); font-size: 14px; font-weight: 400;
  }
  .company-dot { width: 10px; height: 10px; border-radius: 50%; background: var(--brand-red); }
  .job-location { font-size: 12px; margin-top: 10px; }
  .job-salary { font-size: 13px; font-weight: 400; }
  .job-salary span { font-weight: 300; font-size: 11px; }
  .section-label { color: var(--accent-cyan); font-size: 14px; margin-top: 16px; letter-spacing: .3px; }
  .friend-list { display: flex; gap: 14px; margin-top: 10px; }
  .friend { text-align: center; font-size: 10px; color: var(--text-muted); }
  .friend-photo { width: 46px; height: 46px; border-radius: 50%; margin-bottom: 3px; }
  .job-description { font-size: 12.5px; line-height: 1.75; color: var(--text-muted); margin-top: 8px; }
  .skills { display: flex; align-items: flex-end; gap: 22px; margin-top: 20px; }
  .skills .section-label { margin-top: 0; }
  .skill { font-size: 12px; color: var(--text-muted); }
  .skill-bar { width: 48px; height: 4px; border-radius: 2px; margin-bottom: 5px; }
  .actions {
    position: absolute; top: 590px; left: 0; right: 0;
    display: flex; justify-content: space-around; padding: 0 24px;
  }
  .action-button {
    width: 80px; height: 80px; border-radius: 50%;
    border: 1.5px solid #fff; display: flex; align-items: center; justify-content: center;
    font-size: 15px; letter-spacing: .5px;
  }
</style>
</head>
<body>
<main class="app-screen">
  <div class="status-bar">
    <div class="status-carrier">
      <span>●●●○○</span><span>Cellu</span>
      <svg width="12" height="9" viewBox="0 0 12 9"><path d="M1 3.5a7 7 0 0 1 10 0M3 5.5a4 4 0 0 1 6 0" stroke="#fff" stroke-width="1.3" fill="none"/><circle cx="6" cy="7.5" r="1.1" fill="#fff"/></svg>
    </div>
    <span>1:23 AM</span>
    <div class="status-battery">
      <span>77%</span>
      <svg width="22" height="10" viewBox="0 0 22 10"><rect x="0.5" y="0.5" width="18" height="9" rx="2" stroke="#fff" fill="none"/><rect x="2" y="2" width="13" height="6" fill="#fff"/><rect x="19.5" y="3" width="2" height="4" fill="#fff"/></svg>
    </div>
  </div>

  <header class="header">
    <svg class="header-close" width="20" height="20" viewBox="0 0 20 20"><path d="M2 2L18 18M18 2L2 18" stroke="#fff" stroke-width="1.8"/></svg>
    <h1 class="header-title">JOB DETAILS</h1>
    <svg class="header-exit" width="22" height="20" viewBox="0 0 22 20"><path d="M8 5V2h12v16H8v-3" stroke="#fff" stroke-width="1.5" fill="none"/><path d="M14 10H2M6 6l-4 4 4 4" stroke="#fff" stroke-width="1.5" fill="none"/></svg>
  </header>

  <div class="peek-card peek-left"></div>
  <div class="peek-card peek-right"></div>

  <article class="job-card">
    <div class="card-top">
      <h2 class="job-title">SOFTWARE ENGINEERS</h2>
      <div class="company-name"><span class="company-dot"></span>Maribel Beans</div>
    </div>
    <p class="job-location">Singapore</p>
    <p class="job-salary">$80k - $90k <span>per annum</span></p>

    <h3 class="section-label">FRIENDS WORKING / WORKED HERE :</h3>
    <div class="friend-list">
      <div class="friend"><div class="friend-photo" role="img" aria-label="Profile photo of Rita" style="background:linear-gradient(135deg,var(--avatar-warm),var(--avatar-deep))"></div>Rita</div>
      <div class="friend"><div class="friend-photo" role="img" aria-label="Profile photo of James" style="background:linear-gradient(135deg,var(--avatar-cool),var(--avatar-deep))"></div>James</div>
      <div class="friend"><div class="friend-photo" role="img" aria-label="Profile photo of Mia" style="background:linear-gradient(135deg,var(--avatar-olive),var(--avatar-deep))"></div>Mia</div>
      <div class="friend"><div class="friend-photo" role="img" aria-label="Profile photo of Mark" style="background:linear-gradient(135deg,var(--avatar-deep),var(--avatar-light))"></div>Mark</div>
      <div class="friend"><div class="friend-photo" role="img" aria-label="Profile photo of Stacey" style="background:linear-gradient(135deg,var(--avatar-light),var(--avatar-cool))"></div>Stacey</div>
    </div>

    <h3 class="section-label">JOB DESCRIPTION :</h3>
    <p class="job-description">Lorem ipsum dolor sit amet, consectetur adipisicing elit, sed do eiusmod tempor incididunt ut labore et dolore magna aliqua. Ut enim ad minim veniam, quis nostrud exercitation ullamco laboris nisi ut aliquip ex ea commodo consequat. Duis aute irure dolor in reprehenderit in voluptate velit esse cillum dolore eu fugiat nulla pariatur.</p>

    <div class="skills">
      <h3 class="section-label">SKILLS :</h3>
      <div class="skill"><div class="skill-bar" style="background:var(--skill-blue)"></div>PHP</div>
      <div class="skill"><div class="skill-bar" style="background:var(--skill-pink)"></div>JAVA</div>
      <div class="skill"><div class="skill-bar" style="background:var(--skill-green)"></div>C++</div>
    </div>
  </article>

  <nav class="actions">
    <div class="action-button">SKIP</div>
    <div class="action-button">APPLY</div>
    <div class="action-button">NEXT</div>
  </nav>
</main>
</body>
</html>
```